I need a compelling, relevant cover for a book being published in January - title is the name of this project. The book is a call to action to women to become entrepreneurs as today's best path to achieving parity, purpose, prosperity and passion. See extended description of the book's message online at:
walkingtallneverrequireswalkingalone.example
(and attached pdf -- the cover art posted here is simply a placeholder/clip art ). I'm looking for something more emotional and exciting and distinctive and appropriate to the subject matter and message..
type on cover must include:
Standing Tall Won't Require Standing Alone
By Marcia T. Vellby
How Trusting Your Own Instincts Can Shift Your Path and Build Your Venture
With a Foreword by CEO Dorinda P. Halvorsen

Target Market(s)

Professional women, women business owners, aspiring women students, marketers who target women in business, such as IT providers; lenders and funders; financial services like credit card issuers -- anyone who sells to women i biz. Women's networking groups,entrepreneurship divisions at universities, and associations. International audience but tilted toward US readers.

Industry/Entity Type

Call

Font styles to use
Serif

Requirements
Nice to have
• Something that stands out from the crowd -- that would make a woman want to pick up the book because it "speaks" her language/values. Something that addresses contemporary, up-to-date ideas about gender equity/sex roles/women's advancement
Should not have
• NOTHING PINK! Please avoid "empowerment" looks and ideas (too cliche) and avoid traditional business images, like briefcases

```html
<!DOCTYPE html>
<html lang="en">
<head>
<meta charset="utf-8">
<title>Standing Tall Won't Require Standing Alone — Book Cover</title>
<link rel="stylesheet" href="https://fonts.googleapis.com/css2?family=Passion+One:wght@700&family=Parisienne&family=Open+Sans:wght@400&display=swap">
<style>
  :root {
    --paper: #ffffff;
    --ink: #3a3a3c;
    --accent: #e8372a;
    --script-ink: #4a4a4a;
    --board-light: #e9e9e9;
    --board-mid: #8d8d8d;
    --board-dark: #2b2b2b;
  }
  html, body {
    margin: 0;
    padding: 0;
    overflow: hidden;
    background: var(--paper);
  }
  .cover {
    position: relative;
    width: 849px;
    height: 1200px;
    overflow: hidden;
    background: var(--paper);
  }
  .chess-scene {
    position: absolute;
    left: 0;
    top: 905px;
    width: 849px;
    height: 295px;
    background:
      linear-gradient(to bottom, var(--paper) 0%, rgba(255,255,255,0) 40%),
      linear-gradient(to right, var(--board-dark) 0%, var(--board-mid) 45%, var(--board-light) 100%);
  }
  .title-ring {
    position: absolute;
    inset: 0;
    width: 849px;
    height: 1200px;
    pointer-events: none;
  }
  .title {
    position: absolute;
    top: 30px;
    left: 0;
    width: 849px;
    margin: 0;
    text-align: center;
    font-family: "Passion One", "Arial Black", sans-serif;
    font-weight: 700;
    font-size: 100px;
    line-height: 118px;
    letter-spacing: 3px;
    text-transform: uppercase;
    color: var(--ink);
    white-space: nowrap;
  }
  .title .line { display: block; }
  .title .highlight { color: var(--accent); }
  .subtitle {
    position: absolute;
    top: 566px;
    left: 0;
    width: 849px;
    margin: 0;
    text-align: center;
    font-family: "Parisienne", cursive;
    font-weight: 400;
    font-size: 36px;
    line-height: 50px;
    color: var(--script-ink);
    white-space: nowrap;
  }
  .subtitle .line { display: block; }
  .subtitle .highlight { color: var(--accent); font-size: 42px; }
  .credits {
    position: absolute;
    top: 812px;
    right: 26px;
    margin: 0;
    text-align: right;
    font-family: "Open Sans", Arial, sans-serif;
    color: var(--script-ink);
    white-space: nowrap;
  }
  .credits .author {
    display: block;
    font-size: 20px;
    line-height: 42px;
  }
  .credits .foreword {
    display: block;
    font-size: 17px;
    line-height: 36px;
  }
  .credits .name {
    font-family: "Parisienne", cursive;
    color: var(--accent);
  }
  .credits .author .name { font-size: 30px; }
  .credits .foreword .name { font-size: 24px; }
</style>
</head>
<body>
  <main class="cover">
    <div class="chess-scene" role="img" aria-label="Photograph of black and white chess pieces on a board, a black king standing tall beside a fallen white king"></div>

    <svg class="title-ring" viewBox="0 0 849 1200" aria-hidden="true">
      <ellipse cx="425" cy="215" rx="520" ry="310" fill="none" stroke="var(--accent)" stroke-width="3"/>
    </svg>

    <h1 class="title">
      <span class="line">Standing Tall</span>
      <span class="line">Won't Require</span>
      <span class="line">Standing</span>
      <span class="line highlight">Alone</span>
    </h1>

    <p class="subtitle">
      <span class="line">How Trusting</span>
      <span class="line">Your Own <span class="highlight">Instincts</span></span>
      <span class="line">Can Shift Your Path and Build Your Venture</span>
    </p>

    <p class="credits">
      <span class="author">By <span class="name">Marcia T. Vellby</span></span>
      <span class="foreword">With a Foreword by CEO <span class="name">Dorinda P. Halvorsen</span></span>
    </p>
  </main>
</body>
</html>
```